OLVAK Web Design (Need help to re-design our website)

We need someone to help us re-design our website and launch it. All contents for the website are ready. (https://olvak.example.au/)

-Rearrange categories:
1. Heating & Cooling
2. Remove Home Appliance
3. Remove Entertainment

Home page - redesign (It will be a nice touch if the banner is in the loop).

NOTE:
-Brand colour blue and orange.
-Try using professional fonts (Example: Helvetica, etc.)
-The website's Footer should be readable and use light colour.

Target Market(s)

Residentials & commercial buildings

Industry/Entity Type

Heat Ventilation and Cooling Industry, Technology , Renewables

Coding

Coded - Design and coding required

Colors
0094D4
00A9DD
6FCCEA
C7EBF8
E9F6FB
59FF00
82FF00
B8FF75
E3FFCB
F4FFEA
F0912C
F2A743
F7CA91
FBE8D2
FDF5EE

Requirements
Nice to have
• Effects/transition on the words/copy/images.

```html
<!DOCTYPE html>
<html lang="en">
<head>
<meta charset="utf-8">
<title>OLVAK – Heating &amp; Cooling</title>
<link href="https://fonts.googleapis.com/css2?family=Archivo:wght@500;600;700;800&family=Arimo:wght@400;700&display=swap" rel="stylesheet">
<style>
:root{
  --blue:#1362b6;
  --blue-dark:#0d4f99;
  --orange:#f28a1c;
  --orange-light:#f7a23f;
  --grey-band:#ebedf0;
  --text:#555b63;
  --white:#ffffff;
  --head:"Archivo",Arial,sans-serif;
  --body:"Arimo",Helvetica,Arial,sans-serif;
}
*{margin:0;padding:0;box-sizing:border-box}
html,body{width:1200px;height:3264px;overflow:hidden}
body{position:relative;background:var(--white);font-family:var(--body);color:var(--text)}
.abs{position:absolute}
.brand{display:flex;align-items:center;gap:8px;font-family:var(--head);font-weight:800;color:var(--blue);letter-spacing:2px}
.brand .mark{width:24px;height:24px;background:var(--orange)}
.pill{display:inline-flex;align-items:center;justify-content:center;gap:6px;font-family:var(--head);font-weight:700;font-size:12px;letter-spacing:.6px;color:var(--white);background:var(--orange);border-radius:24px 4px 24px 4px;text-transform:uppercase}
.pill.blue{background:var(--blue)}
.arrow{width:14px;height:8px}

/* header */
.topbar{left:0;top:0;width:1200px;height:44px;background:var(--white)}
.topbar .brand{position:absolute;left:122px;top:8px;font-size:26px}
.search{position:absolute;left:334px;top:8px;width:275px;height:28px;border:1px solid #9aa4b1;border-radius:3px;font-size:11px;color:#9aa4b1;padding:7px 8px}
.search svg{position:absolute;right:7px;top:6px}
.contact-row{position:absolute;left:636px;top:11px;display:flex;gap:22px;font-size:12px;color:#333}
.contact-row span{display:flex;align-items:center;gap:6px}
.ico{width:20px;height:20px;border:1.5px solid var(--blue);border-radius:50%;display:inline-block}
.socials{position:absolute;left:995px;top:11px;display:flex;gap:6px}
.navbar{left:0;top:44px;width:1200px;height:30px;background:var(--blue)}
.navbar ul{list-style:none;display:flex;position:absolute;left:123px;top:9px;font-size:11px;color:var(--white)}
.navbar li{margin-right:64px}
.navbar li.active{color:var(--orange-light)}
.book{position:absolute;left:920px;top:44px;width:158px;height:30px;border-radius:18px 0 18px 0;font-size:12px}

/* hero */
.hero{left:0;top:74px;width:1200px;height:538px;overflow:hidden}
.hero-photo{position:absolute;inset:0;background:linear-gradient(100deg,#3a3f3a 0%,#5a5f55 35%,#8b8f88 60%,#3d4a3c 100%)}
.hero h1{position:absolute;left:119px;top:166px;font-family:var(--head);font-weight:800;font-size:45px;line-height:48px;color:var(--white)}
.hero h2{position:absolute;left:119px;top:265px;font-family:var(--head);font-weight:700;font-size:28px;color:var(--white);letter-spacing:.5px}
.hero .pill{position:absolute;left:121px;top:323px;width:140px;height:38px}

/* segments */
.segment{top:675px;width:469px;height:237px;display:flex;overflow:hidden}
.segment .photo{width:245px;height:100%}
.segment .info{width:224px;height:100%;display:flex;flex-direction:column;align-items:center;padding-top:28px;color:var(--white);text-align:center}
.segment .badge{width:54px;height:54px;border-radius:50%;background:var(--white);margin-bottom:10px;display:flex;align-items:center;justify-content:center}
.segment h3{font-family:var(--head);font-weight:700;font-size:25px;margin-bottom:8px}
.segment p{font-size:11.5px;line-height:15px;margin-bottom:14px}
.segment .pill{width:172px;height:38px}
.seg-res{left:120px;border-radius:0 0 0 0}
.seg-res .info{background:var(--orange)}
.seg-com{left:608px;border-radius:0 0 40px 0}
.seg-com .info{background:var(--blue)}

/* products */
.products{left:0;top:974px;width:1200px;height:451px;overflow:hidden}
.products h2{position:absolute;left:0;width:1200px;top:50px;text-align:center;font-family:var(--head);font-weight:700;font-size:36px;color:var(--white)}
.tile{position:absolute;top:112px;width:226px;height:271px;border-radius:36px 0 0 0;overflow:hidden}
.tile .cap{position:absolute;left:0;right:0;bottom:18px;text-align:center;color:var(--white);font-family:var(--head);font-weight:700;font-size:15px}
.tile .cap svg{display:block;margin:4px auto 0}

/* about */
.about-img{left:120px;top:1489px;width:465px;height:336px}
.about{left:703px;top:1497px;width:380px}
.about h2{display:flex;align-items:center;gap:8px;font-family:var(--head);font-weight:700;font-size:36px;color:var(--blue);margin-bottom:14px}
.about h2 .mark{width:22px;height:30px;background:var(--orange)}
.about p{font-size:11.5px;line-height:15.8px;color:#666;margin-bottom:15px}
.about .pill{width:218px;height:40px;margin-top:12px}

/* testimonials */
.reviews{left:0;top:1888px;width:1200px;height:395px;background:var(--grey-band)}
.reviews h2{position:absolute;width:1200px;top:50px;text-align:center;font-family:var(--head);font-weight:700;font-size:33px;color:var(--blue)}
.review{position:absolute;top:111px;width:306px;height:221px;background:var(--white);border-right:4px solid var(--blue);border-bottom:4px solid var(--blue);border-radius:0 0 0 36px;padding:28px 36px}
.review .who{display:flex;align-items:center;gap:12px;margin-bottom:20px}
.avatar{width:50px;height:50px;border-radius:50%;background:#4f5a6a}
.review .name{font-family:var(--head);font-weight:600;font-size:16px;color:#222}
.review .role{font-size:11.5px;color:#444;margin-top:2px}
.review p{font-size:11.5px;line-height:15px;color:#555;margin-bottom:8px}
.stars{color:#f7b500;font-size:15px;letter-spacing:4px}
.nav-dot{position:absolute;top:230px;width:26px;height:26px;border-radius:50%;background:var(--orange);display:flex;align-items:center;justify-content:center}

/* compliance */
.compliance h2{position:absolute;left:0;width:1147px;top:2328px;text-align:center;font-family:var(--head);font-weight:700;font-size:33px;color:var(--blue)}
.seal{position:absolute;top:2386px;width:124px;height:124px;border-radius:50%}
.skyline{left:0;top:2534px;width:1200px;height:100px;background:linear-gradient(#ffffff,#d9dde2)}

/* contact */
.contact{left:0;top:2629px;width:1200px;height:376px;background:linear-gradient(90deg,#f07f12,#f49a35);overflow:hidden}
.contact-photo{left:120px;top:2591px;width:197px;height:414px}
.contact h2{position:absolute;left:437px;top:62px;font-family:var(--head);font-weight:700;font-size:33px;color:var(--white)}
.field{position:absolute;height:30px;border:1px solid rgba(255,255,255,.9);font-size:11.5px;color:var(--white);padding:8px 12px}
.contact .pill{position:absolute;left:446px;top:285px;width:171px;height:38px}

/* footer */
.footer{left:0;top:3005px;width:1200px;height:259px;background:var(--blue);color:var(--white)}
.footer .brand{position:absolute;left:121px;top:50px;font-size:26px;color:var(--white)}
.footer .about-txt{position:absolute;left:121px;top:92px;width:190px;font-size:9px;line-height:14px}
.fcol{position:absolute;top:55px}
.fcol h4{font-family:var(--head);font-weight:700;font-size:15px;margin-bottom:16px}
.fcol ul{list-style:none;font-size:9.5px}
.fcol li{margin-bottom:13px;display:flex;align-items:center;gap:10px}
.fcol li .dot{width:18px;height:18px;border-radius:50%;background:var(--white);flex:none}
.vline{position:absolute;top:50px;width:1px;height:160px;background:rgba(255,255,255,.35)}
.newsletter{position:absolute;left:928px;top:90px;width:140px;font-size:9px;line-height:13px}
.email-box{position:absolute;left:928px;top:122px;width:142px;height:27px;border:1px solid var(--white);font-size:9px;padding:8px 10px}
.footer .pill{position:absolute;left:928px;top:161px;width:142px;height:38px}
.copy{position:absolute;left:0;width:1200px;top:237px;text-align:center;font-size:9px;border-top:1px solid rgba(255,255,255,.35);padding-top:7px}
</style>
</head>
<body>

<header class="abs topbar">
  <div class="brand"><span class="mark"></span>OLVAK</div>
  <div class="search">Search
    <svg width="14" height="14" viewBox="0 0 14 14"><circle cx="6" cy="6" r="4.5" fill="none" stroke="#1362b6" stroke-width="1.5"/><line x1="9.5" y1="9.5" x2="13" y2="13" stroke="#1362b6" stroke-width="1.5"/></svg>
  </div>
  <div class="contact-row">
    <span><i class="ico"></i>Login</span>
    <span><i class="ico"></i>1800 555 010</span>
    <span><i class="ico"></i>info@olvak.example.au</span>
  </div>
  <div class="socials"><i class="ico"></i><i class="ico"></i><i class="ico"></i></div>
</header>
<nav class="abs navbar">
  <ul><li class="active">Home</li><li>Heating &amp; Cooling ⌄</li><li>Our Story</li><li>Support</li></ul>
  <span class="pill book">Book Appointment</span>
</nav>

<section class="abs hero">
  <div class="hero-photo" role="img" aria-label="Outdoor heat pump unit and hot water tanks beside a modern house terrace"></div>
  <svg class="abs" style="left:0;top:0" width="1200" height="538" viewBox="0 0 1200 538"><path d="M1200 370 C1150 460 1080 500 990 512 L1060 538 L1200 538 Z" fill="#f28a1c"/><path d="M1200 0 L1200 370 C1150 460 1080 500 990 512 L1040 515 C1120 500 1180 450 1200 400 Z" fill="#f7a23f" opacity=".0"/></svg>
  <h1>Revolutionise<br>Heating &amp; Cooling</h1>
  <h2>Industry Australiawide</h2>
  <span class="pill">Explore <svg class="arrow" viewBox="0 0 14 8"><path d="M0 4h12M9 1l3 3-3 3" stroke="#fff" fill="none" stroke-width="1.4"/></svg></span>
</section>

<section class="abs segment seg-res">
  <div class="photo" role="img" aria-label="Bright modern living and dining room interior" style="background:linear-gradient(135deg,#d8d6d2,#a9a49b 60%,#6f6a63)"></div>
  <div class="info">
    <div class="badge"><svg width="30" height="28" viewBox="0 0 30 28"><path d="M3 14L15 3l12 11M7 12v13h16V12" fill="none" stroke="#f28a1c" stroke-width="2.4"/></svg></div>
    <h3>Residentials</h3>
    <p>Offering complete solutions for<br>your Residential requirements.</p>
    <span class="pill blue">Get Started <svg class="arrow" viewBox="0 0 14 8"><path d="M0 4h12M9 1l3 3-3 3" stroke="#fff" fill="none" stroke-width="1.4"/></svg></span>
  </div>
</section>
<section class="abs segment seg-com">
  <div class="info">
    <div class="badge"><svg width="26" height="28" viewBox="0 0 26 28"><rect x="5" y="3" width="16" height="23" fill="none" stroke="#1362b6" stroke-width="2.4"/><path d="M9 8h2M15 8h2M9 13h2M15 13h2M9 18h2M15 18h2" stroke="#1362b6" stroke-width="2"/></svg></div>
    <h3>Commercial</h3>
    <p>Offering complete solutions<br>for your business requirements.</p>
    <span class="pill">Get Started <svg class="arrow" viewBox="0 0 14 8"><path d="M0 4h12M9 1l3 3-3 3" stroke="#fff" fill="none" stroke-width="1.4"/></svg></span>
  </div>
  <div class="photo" role="img" aria-label="Modern glass office building lit at dusk" style="background:linear-gradient(160deg,#4a6fa6,#7a8aa0 45%,#c9a85f 75%,#4e4a40)"></div>
</section>

<section class="abs products">
  <svg class="abs" style="left:0;top:0" width="1200" height="451" viewBox="0 0 1200 451"><path d="M0 0H1200V451H0Z" fill="#1362b6"/><path d="M0 210 C40 90 160 10 340 0 L0 0Z" fill="#ffffff"/><path d="M0 210 C40 90 160 10 340 0 L310 0 C170 18 60 90 0 250Z" fill="#f28a1c"/><path d="M0 250 C20 200 40 170 60 150 L0 330Z" fill="#f28a1c" opacity=".9"/></svg>
  <h2>Heating &amp; Cooling</h2>
  <div class="tile" style="left:122px" role="img" aria-label="Heat pump water tank against a brick wall"><div style="position:absolute;inset:0;background:linear-gradient(160deg,#b58a74,#8a6454 60%,#3c2c26)"></div><div class="cap">Heat Pump<svg width="14" height="8" viewBox="0 0 14 8"><path d="M0 4h12M9 1l3 3-3 3" stroke="#fff" fill="none" stroke-width="1.4"/></svg></div></div>
  <div class="tile" style="left:365px" role="img" aria-label="Wall mounted split air conditioner"><div style="position:absolute;inset:0;background:linear-gradient(160deg,#d8dcd6,#b7c2c0 55%,#6e7a76)"></div><div class="cap">Air Conditioners<svg width="14" height="8" viewBox="0 0 14 8"><path d="M0 4h12M9 1l3 3-3 3" stroke="#fff" fill="none" stroke-width="1.4"/></svg></div></div>
  <div class="tile" style="left:608px" role="img" aria-label="Swimming pool heat pump unit by a pool"><div style="position:absolute;inset:0;background:linear-gradient(160deg,#9aa7a4,#c7ccc8 50%,#6c7873)"></div><div class="cap">Swimming Pool Heat Pump<svg width="14" height="8" viewBox="0 0 14 8"><path d="M0 4h12M9 1l3 3-3 3" stroke="#fff" fill="none" stroke-width="1.4"/></svg></div></div>
  <div class="tile" style="left:851px" role="img" aria-label="Monoblock heat pump outdoor unit"><div style="position:absolute;inset:0;background:linear-gradient(160deg,#e3e5e4,#b4b9b7 55%,#5a605d)"></div><div class="cap">Monoblock Heat Pump<svg width="14" height="8" viewBox="0 0 14 8"><path d="M0 4h12M9 1l3 3-3 3" stroke="#fff" fill="none" stroke-width="1.4"/></svg></div></div>
</section>

<svg class="abs about-img" viewBox="0 0 465 336" role="img" aria-label="Household appliances and electronics arranged in a living room">
  <defs><linearGradient id="app" x1="0" y1="0" x2="1" y2="1"><stop offset="0" stop-color="#c8b9a4"/><stop offset=".5" stop-color="#6f6b68"/><stop offset="1" stop-color="#8e6a47"/></linearGradient></defs>
  <path d="M303 12 C340 2 400 0 465 0 C460 30 440 50 390 56 L300 56 Z" fill="#1362b6"/>
  <path d="M0 270 C0 150 60 70 150 70 L300 70 C350 70 420 40 465 10 L465 230 C440 270 400 270 380 270 Z" fill="url(#app)"/>
  <path d="M8 336 C8 300 30 282 70 282 L170 282 C160 315 140 336 110 336 Z" fill="#1362b6"/>
</svg>
<section class="abs about">
  <h2><span class="mark"></span>About Our Story</h2>
  <p>OLVAK is a company dedicated to manufacturing and installing energy-efficient products that reduce energy consumption, save costs, and promote sustainability. Our mission is to help individuals and businesses reduce their carbon footprint while also enhancing their comfort and quality of life.</p>
  <p>Our story began with a group of like-minded individuals who saw the urgent need to address climate change and the impact of energy consumption on the environment. We recognized that energy-efficient products were not only good for the planet but also for individuals' wallets. We believed that we could make a difference by developing and providing accessible and affordable energy-efficient solutions.</p>
  <span class="pill">Explore Our Story <svg class="arrow" viewBox="0 0 14 8"><path d="M0 4h12M9 1l3 3-3 3" stroke="#fff" fill="none" stroke-width="1.4"/></svg></span>
</section>

<section class="abs reviews">
  <h2>What Our Clients Says</h2>
  <span class="nav-dot" style="left:71px"><svg width="10" height="12" viewBox="0 0 10 12"><path d="M7 1L2 6l5 5" stroke="#fff" fill="none" stroke-width="2"/></svg></span>
  <article class="review" style="left:120px">
    <div class="who"><div class="avatar" role="img" aria-label="Client portrait"></div><div><div class="name">Jane Doyle</div><div class="role">Our Clients</div></div></div>
    <p>Lorem ipsum dolor sit amet, consectetur adipiscing elit. Quisque id fringilla odio, non efficitur dui. Suspendisse eu cosquat lacus, vel scelerisque leo.</p>
    <div class="stars">★★★★★</div>
  </article>
  <article class="review" style="left:446px">
    <div class="who"><div class="avatar" role="img" aria-label="Client portrait"></div><div><div class="name">Jane Doyle</div><div class="role">Our Clients</div></div></div>
    <p>Lorem ipsum dolor sit amet, consectetur adipiscing elit. Quisque id fringilla odio, non efficitur dui. Suspendisse eu cosquat lacus, vel scelerisque leo.</p>
    <div class="stars">★★★★★</div>
  </article>
  <article class="review" style="left:772px">
    <div class="who"><div class="avatar" role="img" aria-label="Client portrait"></div><div><div class="name">Jane Doyle</div><div class="role">Our Clients</div></div></div>
    <p>Lorem ipsum dolor sit amet, consectetur adipiscing elit. Quisque id fringilla odio, non efficitur dui. Suspendisse eu cosquat lacus, vel scelerisque leo.</p>
    <div class="stars">★★★★★</div>
  </article>
  <span class="nav-dot" style="left:1101px"><svg width="10" height="12" viewBox="0 0 10 12"><path d="M3 1l5 5-5 5" stroke="#fff" fill="none" stroke-width="2"/></svg></span>
</section>

<section class="compliance">
  <h2>Fully Compliant with all Government Rebates</h2>
  <div class="seal" style="left:290px;background:#dfe4ee;border:3px solid #1b3f8a" role="img" aria-label="Australian owned and operated badge"></div>
  <div class="seal" style="left:538px;background:radial-gradient(circle,#1f6b3a 45%,#d6b23c 47%)" role="img" aria-label="Premium quality seal"></div>
  <div class="seal" style="left:812px;background:#eef0f2;border:3px solid #f5a623" role="img" aria-label="Save energy badge"></div>
</section>
<div class="abs skyline" role="img" aria-label="Faint city skyline"></div>

<section class="abs contact">
  <svg class="abs" style="left:0;top:0" width="1200" height="376" viewBox="0 0 1200 376"><path d="M1000 0 C1110 10 1180 60 1200 120 L1200 0Z" fill="#ffffff"/><path d="M1000 0 C1100 12 1170 60 1200 110 L1200 200 C1180 110 1110 40 1020 10Z" fill="#1362b6"/></svg>
  <h2>Get In Touch</h2>
  <div class="field" style="left:438px;top:110px;width:312px">First Name</div>
  <div class="field" style="left:764px;top:110px;width:312px">Enter Email</div>
  <div class="field" style="left:438px;top:155px;width:312px">Enter Phone</div>
  <div class="field" style="left:764px;top:155px;width:312px">Address</div>
  <div class="field" style="left:438px;top:198px;width:638px;height:68px">Message</div>
  <span class="pill blue">Submit <svg class="arrow" viewBox="0 0 14 8"><path d="M0 4h12M9 1l3 3-3 3" stroke="#fff" fill="none" stroke-width="1.4"/></svg></span>
</section>
<div class="abs contact-photo" role="img" aria-label="Two white heat pump hot water tanks" style="background:linear-gradient(90deg,#cfd3d6,#f4f5f6 45%,#c2c6c9);border-radius:14px 14px 0 0"></div>

<footer class="abs footer">
  <div class="brand"><span class="mark"></span>OLVAK</div>
  <p class="about-txt">OLVAK is a company dedicated to manufacturing and installing energy-efficient products that reduce energy consumption, save costs, and promote sustainability. Our mission is to help individuals and businesses reduce their carbon footprint while also enhancing their comfort and quality of life.</p>
  <span class="vline" style="left:330px"></span>
  <div class="fcol" style="left:366px"><h4>Quick links</h4><ul><li>Home</li><li>Heating &amp; Cooling</li><li>Our Story</li><li>Support</li></ul></div>
  <span class="vline" style="left:510px"></span>
  <div class="fcol" style="left:530px"><h4>Contact Us</h4><ul><li><i class="dot"></i>1800 555 010</li><li><i class="dot"></i>info@olvak.example.au</li><li><i class="dot"></i>120 Sample Rd, Newtown VIC 3000</li><li><i class="dot"></i>9AM - 5PM (Mon - Fri)</li></ul></div>
  <span class="vline" style="left:728px"></span>
  <div class="fcol" style="left:776px"><h4>Follow us</h4><ul><li><i class="dot"></i>Friendbook</li><li><i class="dot"></i>Snapgram</li><li><i class="dot"></i>Worklink</li></ul></div>
  <span class="vline" style="left:885px"></span>
  <div class="fcol" style="left:928px"><h4>Stay Connected</h4></div>
  <p class="newsletter">Enter your email address to register to our newsletter subscription</p>
  <div class="email-box">Enter Your Email</div>
  <span class="pill">Subscribe <svg class="arrow" viewBox="0 0 14 8"><path d="M0 4h12M9 1l3 3-3 3" stroke="#fff" fill="none" stroke-width="1.4"/></svg></span>
  <div class="copy">© Copyright 2024 OLVAK All Rights Reserved.</div>
</footer>

</body>
</html>
```